Professional Single Page Website Design for Velloway Advisory

Velloway Advisory is a new business consultancy specializing in providing expert services to small businesses, primarily in the brick-and-mortar retail and food service sectors. We offer a range of services including franchise development and launch, due diligence, and construction management.

Currently, we have a basic website set up at www.vellowayadvisory.example, but we need a professional touch to enhance its design and functionality.

Project Requirements:
- Single Page Design: For now, we need a single page design that effectively showcases who we are, our services, and contact information.
- Future Expansion: The design should be flexible and scalable for future expansion to include additional pages like specific service offerings, about us, and a dedicated contact page.
- Design Aesthetic: We are looking for a modern yet professional design that aligns with our brand identity.
- Logo: We have a logo that we like, which was also sourced from Pixel Forum. The logo files are attached to this project brief.

Key Sections to Include:
- Hero Section: An engaging introduction to Velloway Advisory with a strong visual impact.
- About Us: A brief overview of who we are and our mission.
- Team: Section for the profiles of the two principals.
- Services: A clear and concise presentation of our services, including franchise development, due diligence, and construction management.
- Contact Information: Easy-to-find contact details, including a form for inquiries.
- Call to Action: Encouraging visitors to get in touch with us for consultations or further information.

Design Considerations:
- Ensure the design is responsive and mobile-friendly.
- Include high-quality images and icons that complement our services and industry.
- We do not need development services, this is only a design project.

```html
<!DOCTYPE html>
<html lang="en">
<head>
<meta charset="utf-8">
<title>Velloway Advisory</title>
<link href="https://fonts.googleapis.com/css2?family=Poppins:wght@300;400;500;600;700&display=swap" rel="stylesheet">
<style>
:root{
  --green:#7fbc9e;
  --green-soft:#a8d3bd;
  --green-pale:#d6ebe0;
  --dark:#1f2a33;
  --ink:#1d1d1f;
  --text:#3a3f44;
  --white:#ffffff;
}
*{box-sizing:border-box;margin:0;padding:0}
html,body{width:1200px;height:3929px;overflow:hidden;background:var(--white)}
body{font-family:'Poppins',sans-serif;color:var(--ink)}
.page{position:relative;width:1200px;height:3929px;overflow:hidden}
.abs{position:absolute}
.brand{display:flex;align-items:center;gap:10px;font-weight:600;color:var(--dark);font-size:20px;white-space:nowrap}
.brand-dot{width:16px;height:16px;border-radius:50%;background:var(--green)}
.nav{top:30px;left:0;width:1200px;height:40px}
.nav-link{position:absolute;top:2px;font-size:15px;color:var(--ink);text-decoration:none}
.nav-link.active{border-bottom:2px solid var(--green);padding-bottom:4px}
.nav-sep{position:absolute;top:2px;font-size:15px;color:#9aa0a6}
.pill{display:inline-block;background:var(--green);color:var(--white);border-radius:22px;font-size:14px;padding:10px 30px;text-decoration:none;white-space:nowrap}
.hero-title{left:103px;top:196px;font-size:44px;font-weight:700;line-height:46px;white-space:nowrap}
.hero-title span{color:var(--green);display:block}
.hero-sub{left:106px;top:346px;font-size:21px;font-weight:500;line-height:27px}
.hero-text{left:106px;top:416px;width:400px;font-size:13px;line-height:19px;color:var(--text);border-left:2px solid var(--green);padding-left:16px}
.section-title{font-size:40px;font-weight:700;white-space:nowrap}
.section-title span{color:var(--green)}
.who-lead{left:601px;top:796px;width:490px;font-size:17px;font-weight:500;line-height:27px}
.who-text{left:602px;top:900px;width:520px;font-size:15px;line-height:24.5px;color:var(--text);border-left:2px solid #c9c9c9;padding-left:17px}
.mission{left:88px;top:1246px;width:1034px;height:511px;border-radius:18px;overflow:hidden;background:var(--dark)}
.mission-photo{position:absolute;right:0;top:0;width:640px;height:511px;background:linear-gradient(90deg,var(--dark) 0%,#4d5b63 35%,#8a7766 65%,#b9c3c8 100%)}
.mission-copy{position:absolute;left:90px;top:126px;width:445px;color:var(--white)}
.eyebrow{font-size:13px;letter-spacing:1.5px;text-transform:uppercase}
.mission-copy h2{font-size:40px;font-weight:600;margin-top:6px}
.underline{width:54px;height:3px;background:var(--green);margin-top:4px}
.mission-copy p{font-size:15px;line-height:25px;margin-top:22px}
.team-band{left:0;top:1650px;width:1200px;height:634px;background:linear-gradient(180deg,var(--green) 0%,var(--green-soft) 100%)}
.card{background:var(--white);box-shadow:0 3px 12px rgba(0,0,0,.08)}
.team-card{top:1905px;width:478px;height:247px}
.team-photo{position:absolute;left:0;top:0;width:200px;height:247px}
.team-info{position:absolute;left:222px;top:36px;width:240px}
.team-info h3{font-size:21px;font-weight:600}
.team-info .role{font-size:18px;color:var(--text)}
.team-info p{font-size:10.5px;line-height:17px;color:var(--text);margin-top:8px}
.socials{display:flex;gap:22px;margin-top:12px}
.socials i{width:13px;height:13px;border:1.5px solid var(--green);border-radius:50%;display:block}
.svc-photo{top:2483px;height:271px;width:325px}
.svc-card{top:2703px;width:290px;height:327px;padding:30px 26px}
.svc-card h3{font-size:18px;font-weight:500;line-height:24px}
.svc-card p{font-size:11.5px;line-height:19.5px;color:var(--text);margin-top:14px}
.svc-card.dark{background:var(--dark);color:var(--white)}
.svc-card.dark p{color:#dfe4e6}
.svc-icon{width:66px;height:66px;border-radius:50%;background:var(--green);border:4px solid var(--white)}
.contact{left:0;top:3128px;width:1200px;height:608px;background:var(--dark);overflow:hidden}
.contact-info{position:absolute;left:154px;top:90px;color:var(--white)}
.contact-info .eyebrow{color:var(--green);font-size:14px}
.contact-info h2{font-size:37px;font-weight:600;margin-top:2px}
.c-row{display:flex;align-items:center;gap:27px;margin-top:34px}
.c-ico{width:48px;height:48px;border-radius:50%;background:var(--green);display:flex;align-items:center;justify-content:center;flex:none}
.c-row .lbl{font-size:17px}
.c-row .val{font-size:17px;color:var(--green-soft);line-height:24px}
.form{position:absolute;left:697px;top:133px;width:366px}
.field{background:var(--white);height:45px;margin-bottom:11px;font-size:13px;color:#555;padding:13px 19px}
.field.msg{height:118px}
.send{display:inline-block;margin-top:17px;background:var(--dark);color:var(--white);border-radius:24px;padding:13px 36px;font-size:13px;font-weight:600}
.footer-links{left:400px;top:3777px;display:flex;gap:68px;font-size:18px;font-weight:500}
.copyright{left:0;top:3866px;width:1200px;text-align:center;font-size:13px;color:var(--text);border-top:1px solid #e5e5e5;padding-top:20px}
</style>
</head>
<body>
<div class="page">

  <!-- Hero -->
  <svg class="abs" style="left:500px;top:0" width="700" height="670" viewBox="0 0 700 670" role="img" aria-label="Photo of a modern commercial retail building under a blue sky">
    <defs>
      <linearGradient id="heroSky" x1="0" y1="0" x2="0" y2="1">
        <stop offset="0" stop-color="#2f63b8"/>
        <stop offset=".5" stop-color="#d8c4a6"/>
        <stop offset=".75" stop-color="#c9814e"/>
        <stop offset="1" stop-color="#8c8f92"/>
      </linearGradient>
    </defs>
    <path d="M150 0 H700 V500 L470 640 Q420 690 370 640 L40 290 Q0 240 40 190 Z" fill="url(#heroSky)"/>
  </svg>
  <div class="abs" style="left:0;top:0;width:620px;height:620px;background:linear-gradient(90deg,#fff 60%,rgba(255,255,255,0))"></div>

  <div class="abs nav">
    <div class="abs brand" style="left:107px;top:2px"><span class="brand-dot"></span>Velloway Advisory</div>
    <a class="nav-link active" style="left:453px">About</a>
    <span class="nav-sep" style="left:523px">|</span>
    <a class="nav-link" style="left:561px">Services</a>
    <span class="nav-sep" style="left:633px">|</span>
    <a class="nav-link" style="left:686px">Team</a>
    <span class="nav-sep" style="left:748px">|</span>
    <a class="nav-link" style="left:792px">Contact</a>
    <a class="abs pill" style="left:915px;top:-3px">Get in touch</a>
  </div>

  <h1 class="abs hero-title">Building Success<span>in Southern</span><span>California</span></h1>
  <div class="abs hero-sub">Expertise at Every Step:<br>From Planning to Execution</div>
  <p class="abs hero-text">At Velloway, we blend innovative strategies with local market expertise to guide your commercial real estate ventures. Whether you're launching a new restaurant, investing in retail spaces, or expanding a franchise</p>
  <a class="abs pill" style="left:103px;top:515px;font-size:13px">Learn More ›</a>

  <!-- Who we are -->
  <svg class="abs" style="left:0;top:625px" width="580" height="750" viewBox="0 0 580 750" role="img" aria-label="Green tinted photo of a brick office building framed in a diamond shape">
    <path d="M0 80 L90 0 H180 L360 180 V700 H0 Z" fill="#9ccbb2"/>
    <path d="M0 640 L90 750 L160 700 Z" fill="#7fbc9e"/>
    <path d="M310 100 Q350 70 390 100 L545 260 Q575 300 545 340 L390 500 Q350 540 310 500 L110 300 Q80 260 110 225 Z" fill="#e4efe9"/>
    <path d="M200 150 L340 80 L520 260 L340 530 L120 320 Z" fill="#cfd8dc" opacity=".6"/>
  </svg>
  <h2 class="abs section-title" style="left:602px;top:720px">Who We <span>Are</span></h2>
  <svg class="abs" style="left:1012px;top:748px" width="188" height="10"><circle cx="6" cy="5" r="5" fill="#7fbc9e"/><line x1="6" y1="5" x2="188" y2="5" stroke="#7fbc9e" stroke-width="1.5"/></svg>
  <p class="abs who-lead">Welcome to Velloway Advisory, your trusted partner in navigating the complexities of the real estate and small business markets.</p>
  <p class="abs who-text">Founded by industry veterans Adrian Solvano and Ethan Sorel, we specialize in providing comprehensive services tailored to the unique needs of our clients. Whether you're a franchisee, a new restaurant owner, or a commercial real estate investor, our expertise in due diligence, construction management, and investment property evaluation ensures you make informed, strategic decisions. Discover how Velloway Advisory can support your business journey. Partner with us and experience the difference our dedication and expertise can make.</p>

  <div class="abs team-band"></div>

  <!-- Mission -->
  <section class="abs mission">
    <div class="mission-photo" role="img" aria-label="Photo of a newly built storefront with wood cladding and a parking lot"></div>
    <div class="mission-copy">
      <div class="eyebrow">Velloway Advisory</div>
      <h2>Our Mission</h2>
      <div class="underline"></div>
      <p>At Velloway Advisory, we are committed to your success. Our approach combines meticulous analysis, strategic insights, and personalized service to help you achieve your business goals. We pride ourselves on our ability to deliver results that exceed expectations, fostering long-term relationships built on trust and excellence.</p>
    </div>
  </section>

  <!-- Team -->
  <h2 class="abs section-title" style="left:0;top:1805px;width:1200px;text-align:center;color:var(--white)">Meet the Team</h2>
  <div class="abs" style="left:570px;top:1867px;width:60px;height:3px;background:var(--white)"></div>

  <article class="abs card team-card" style="left:108px">
    <div class="team-photo" role="img" aria-label="Portrait photo of Adrian Solvano" style="background:linear-gradient(160deg,#a9c3d6,#e9ecef 60%,#c8ced3)"></div>
    <div class="team-info">
      <h3>Adrian Solvano</h3>
      <div class="role">Principal</div>
      <p>Adrian Solvano brings almost 20 years of rich experience as a real estate investor and a pivotal role at one of southern California's largest real estate management firms, where he...</p>
      <div class="socials"><i></i><i></i><i></i></div>
    </div>
  </article>
  <article class="abs card team-card" style="left:601px">
    <div class="team-photo" role="img" aria-label="Portrait photo of Ethan Sorel" style="background:linear-gradient(160deg,#3b4650,#8a7a6c 60%,#2c343b)"></div>
    <div class="team-info" style="left:242px;width:222px">
      <h3>Ethan Sorel</h3>
      <div class="role">Principal</div>
      <p>Ethan Sorel is a seasoned real estate expert with extensive experience in project and construction management, and a licensed real estate agent in California. Fluent in both English and Korean.</p>
      <div class="socials"><i></i><i></i><i></i></div>
    </div>
  </article>

  <!-- Services -->
  <svg class="abs" style="left:598px;top:2250px" width="10" height="70"><line x1="5" y1="0" x2="5" y2="63" stroke="#1f2a33" stroke-width="1.5"/><circle cx="5" cy="64" r="4" fill="#1f2a33"/></svg>
  <h2 class="abs section-title" style="left:0;top:2342px;width:1200px;text-align:center;color:var(--dark)">Velloway <span>Services</span></h2>
  <div class="abs" style="left:584px;top:2404px;width:54px;height:4px;background:var(--green)"></div>

  <div class="abs svc-photo" role="img" aria-label="Photo of wooden blocks with shop icons connected in a network" style="left:88px;background:linear-gradient(135deg,#cfe3e6,#e0b48b 50%,#b9d7d8)"></div>
  <div class="abs svc-photo" role="img" aria-label="Digital graphic of a due diligence interface with icons" style="left:442px;background:radial-gradient(circle at 40% 40%,#3aa7b0,#10333f 70%)"></div>
  <div class="abs svc-photo" role="img" aria-label="Photo of engineers reviewing construction plans with a hard hat on the desk" style="left:785px;background:linear-gradient(135deg,#e9eef1,#c9d3da 50%,#8193a3)"></div>

  <article class="abs card svc-card" style="left:107px">
    <div class="abs svc-icon" style="left:30px;top:-45px"></div>
    <h3 style="margin-top:18px">Franchise development and launch</h3>
    <p>At Velloway Advisory, our Franchise Development &amp; Launch service is designed to transform your successful business into a thriving franchise. We start by thoroughly evaluating your business model to determine its franchisability. Once confirmed, our team handles every aspect of the franchise setup, including legal documentation, branding, marketing strategies, operational guidelines, and franchisee recruitment.</p>
  </article>
  <article class="abs card svc-card dark" style="left:461px">
    <div class="abs svc-icon" style="left:54px;top:-50px"></div>
    <h3 style="margin-top:18px">Due Diligence</h3>
    <p>Velloway offers comprehensive evaluations tailored to your business needs. We meticulously assess franchise opportunities, business sales, and property transactions, identifying potential risks and liabilities to safeguard your investments. Our expert team provides actionable recommendations on deal points and offers strategic guidance throughout the entire process.</p>
  </article>
  <article class="abs card svc-card" style="left:804px">
    <div class="abs svc-icon" style="left:50px;top:-50px"></div>
    <h3 style="margin-top:18px">Construction Management</h3>
    <p>Our Building &amp; Construction Management Services oversee every aspect of your construction and development projects, from initial planning to final completion. We ensure projects stay on time and within budget, providing meticulous attention to detail and proactive problem-solving.</p>
  </article>

  <!-- Contact -->
  <section class="abs contact">
    <div class="abs" role="img" aria-label="Dim photo of a commercial building behind the contact details" style="left:0;top:200px;width:760px;height:408px;background:linear-gradient(180deg,rgba(31,42,51,0),#3b4650)"></div>
    <svg class="abs" style="left:540px;top:0" width="660" height="608" viewBox="0 0 660 608">
      <path d="M205 0 H660 V608 H260 L30 330 Q0 295 30 260 Z" fill="#7fbc9e"/>
    </svg>
    <svg class="abs" style="left:0;top:133px" width="122" height="10"><line x1="0" y1="5" x2="116" y2="5" stroke="#7fbc9e" stroke-width="1.5"/><circle cx="116" cy="5" r="5" fill="#7fbc9e"/></svg>
    <div class="contact-info">
      <div class="eyebrow">Get in touch</div>
      <h2>Contact Velloway</h2>
      <div class="c-row">
        <div class="c-ico"><svg width="22" height="26" viewBox="0 0 22 26"><path d="M11 1a9 9 0 0 0-9 9c0 7 9 15 9 15s9-8 9-15a9 9 0 0 0-9-9z" fill="#1f2a33"/><circle cx="11" cy="10" r="3.5" fill="#7fbc9e"/></svg></div>
        <div><div class="lbl">Address</div><div class="val">214 Harbor Crest Ave,<br>Irvine, CA 92600</div></div>
      </div>
      <div class="c-row">
        <div class="c-ico"><svg width="24" height="18" viewBox="0 0 24 18"><rect x="1" y="1" width="22" height="16" rx="2" fill="#1f2a33"/><path d="M2 2l10 8 10-8" stroke="#7fbc9e" stroke-width="1.6" fill="none"/></svg></div>
        <div><div class="lbl">Email Us</div><div class="val">enquiry@vellowayadvisory.example</div></div>
      </div>
      <div class="c-row">
        <div class="c-ico"><svg width="22" height="22" viewBox="0 0 24 24"><path d="M6.6 10.8a15 15 0 0 0 6.6 6.6l2.2-2.2a1 1 0 0 1 1-.25 11 11 0 0 0 3.6.6 1 1 0 0 1 1 1V20a1 1 0 0 1-1 1A17 17 0 0 1 3 4a1 1 0 0 1 1-1h3.5a1 1 0 0 1 1 1c0 1.25.2 2.45.57 3.57a1 1 0 0 1-.25 1z" fill="#1f2a33"/></svg></div>
        <div><div class="lbl">Phone number</div><div class="val">(+100) 555 0142</div></div>
      </div>
    </div>
    <form class="form">
      <div class="field">Name</div>
      <div class="field">Email address</div>
      <div class="field">Phone</div>
      <div class="field msg">Leave message</div>
      <div class="send">SEND MESSAGE</div>
    </form>
  </section>

  <!-- Footer -->
  <div class="abs brand" style="left:133px;top:3779px;font-size:21px"><span class="brand-dot"></span>Velloway Advisory</div>
  <nav class="abs footer-links"><span>About</span><span>Services</span><span>Team</span><span>Contact</span></nav>
  <div class="abs" style="left:943px;top:3781px;display:flex;gap:20px">
    <span style="width:24px;height:24px;border-radius:50%;background:var(--green);display:block"></span>
    <span style="width:24px;height:24px;border-radius:50%;background:var(--dark);display:block"></span>
    <span style="width:24px;height:24px;background:var(--dark);display:block"></span>
  </div>
  <div class="abs copyright">© 2024 Velloway Advisory | All Right Reserved</div>
</div>
</body>
</html>
```